Vollo Activewear business card design

I need a business card designed for my activewear business. I would like to use the colours pink, purple white and blue. please see attached logo. please include (name) Rosalind Thwaite (phone) 0417285630 (email) rozzivollo@mailbrook.net (ABN) 51837264019 . please include - Free shipping on all orders over $100

Target Market(s)

female

Contact Information for Business Card

Colors

Designer to choose colors to be used in the design.

Requirements
Must have
• I need a business card designed for my activewear business. I would like to use the colours pink, purple white and blue. please see attached logo. please include (name) Rosalind Thwaite (phone) 0417285630 (email) rozzivollo@mailbrook.net (ABN) 51837264019 . please include - Free shipping on all orders over $100

```html
<!DOCTYPE html>
<html lang="en">
<head>
<meta charset="utf-8">
<title>Vollo Activewear – Business Card</title>
<link href="https://fonts.googleapis.com/css2?family=Exo+2:wght@400;500;600;700&display=swap" rel="stylesheet">
<style>
  :root {
    --backdrop: #7d6a55;
    --purple: #8e3596;
    --pink-hot: #ee519b;
    --pink-soft: #f5a6c9;
    --white: #ffffff;
    --ink: #8a2f92;
    --wave-tint: #eeeeee;
  }
  * { margin: 0; padding: 0; box-sizing: border-box; }
  html, body { width: 900px; height: 1200px; overflow: hidden; }
  body {
    background: var(--backdrop);
    font-family: "Exo 2", Arial, sans-serif;
    position: relative;
  }
  .card {
    position: absolute;
    left: 86px;
    width: 736px;
    height: 430px;
    border-radius: 24px;
    overflow: hidden;
    background: var(--white);
  }
  .card-front { top: 136px; }
  .card-back { top: 633px; }

  .front-backdrop {
    position: absolute;
    inset: 0;
    background: radial-gradient(ellipse 62% 78% at 50% 50%,
      var(--pink-soft) 0%, var(--pink-soft) 58%, #e98fc0 72%, var(--purple) 100%);
  }

  .holder-name {
    position: absolute;
    top: 88px; left: 0; width: 736px;
    text-align: center;
    color: var(--ink);
    font-size: 30px;
    font-weight: 600;
  }
  .contact-icons {
    position: absolute;
    top: 182px; left: 208px;
    width: 320px; height: 36px;
  }
  .contact-details {
    position: absolute;
    top: 266px; left: 0; width: 736px;
    text-align: center;
    color: var(--ink);
    font-size: 22px;
    line-height: 33px;
    font-weight: 400;
  }

  .wave-field {
    position: absolute;
    left: 0; top: 40px;
    width: 736px; height: 320px;
    background: linear-gradient(180deg, rgba(238,238,238,0) 0%, var(--wave-tint) 45%, rgba(238,238,238,0) 100%);
  }
  .brand {
    position: absolute;
    top: 150px; left: 0; width: 736px;
    display: flex; align-items: center; justify-content: center;
    gap: 22px;
  }
  .brand-dot {
    width: 46px; height: 46px;
    border-radius: 50%;
    background: var(--pink-soft);
  }
  .brand-name {
    color: var(--purple);
    font-size: 84px;
    font-weight: 700;
    letter-spacing: 2px;
    line-height: 1;
  }
  .shipping-note {
    position: absolute;
    top: 362px; left: 0; width: 736px;
    display: flex; align-items: center; justify-content: center;
    gap: 10px;
    color: var(--pink-hot);
    font-size: 21px;
    font-weight: 600;
  }
  .shipping-note .rule {
    width: 70px; height: 2px;
    background: linear-gradient(90deg, rgba(238,81,155,0), var(--pink-hot));
  }
  .shipping-note .rule.right {
    background: linear-gradient(90deg, var(--pink-hot), rgba(238,81,155,0));
  }
</style>
</head>
<body>

  <section class="card card-front">
    <div class="front-backdrop" role="img" aria-label="Decorative curved pink, purple and white background shapes"></div>

    <h1 class="holder-name">Rosalind Thwaite</h1>

    <svg class="contact-icons" viewBox="0 0 320 36" width="320" height="36" aria-hidden="true">
      <line x1="0" y1="18" x2="70" y2="16" stroke="var(--white)" stroke-width="2"/>
      <line x1="250" y1="16" x2="320" y2="18" stroke="var(--white)" stroke-width="2"/>
      <g transform="translate(104 18)">
        <circle r="18" fill="var(--white)"/>
        <path d="M-6 -9 L-2 -9 L0 -4 L-3 -2 C-2 2 1 5 3 6 L5 3 L10 5 L10 9 C2 10 -9 0 -6 -9 Z" fill="var(--ink)"/>
      </g>
      <g transform="translate(160 18)">
        <circle r="18" fill="var(--white)"/>
        <rect x="-9" y="-6" width="18" height="12" rx="1.5" fill="var(--ink)"/>
        <path d="M-9 -5 L0 2 L9 -5" fill="none" stroke="var(--white)" stroke-width="1.5"/>
      </g>
      <g transform="translate(216 18)" fill="none" stroke="var(--ink)" stroke-width="1.6">
        <circle r="18" fill="var(--white)" stroke="none"/>
        <circle r="9"/>
        <ellipse rx="4" ry="9"/>
        <line x1="-9" y1="0" x2="9" y2="0"/>
        <line x1="-8" y1="-4.5" x2="8" y2="-4.5"/>
        <line x1="-8" y1="4.5" x2="8" y2="4.5"/>
      </g>
    </svg>

    <p class="contact-details">
      041 728 5630<br>
      rozzivollo@mailbrook.net<br>
      (ABN) 51837264019
    </p>
  </section>

  <section class="card card-back">
    <div class="wave-field" role="img" aria-label="Soft grey flowing wave-line background pattern"></div>
    <div class="brand">
      <span class="brand-dot"></span>
      <span class="brand-name">VOLLO</span>
    </div>
    <p class="shipping-note">
      <span class="rule"></span>
      Free shipping on all orders over $100
      <span class="rule right"></span>
    </p>
  </section>

</body>
</html>
```